A label for my commercially sold local honey. This is a LABEL not a logo

3 inches high
2 inches wide

Target Market(s)

Customers who like "local" honey

Logo Text

Wildflower Honey -- 100% Pure & Unfiltered -- Florida

Logo styles of interest
Wordmark Logo
Requirements
Must have
• Wildflower Honey -- 100% Pure & Unfiltered -- Florida

Florida should be dominant

3 inches high / 2 inches wide

```html
<!DOCTYPE html>
<html lang="en">
<head>
<meta charset="utf-8">
<title>Wildflower Honey Label</title>
<link rel="stylesheet" href="https://fonts.googleapis.com/css2?family=Stint+Ultra+Condensed&family=Permanent+Marker&family=Open+Sans:wght@400&display=swap">
<style>
  :root {
    --page: #ffffff;
    --honey: #f9d229;
    --honey-light: #fbdc4a;
    --honey-deep: #e0a91c;
    --ink: #2f2e33;
    --white: #ffffff;
  }
  * { box-sizing: border-box; margin: 0; padding: 0; }
  html, body {
    width: 1200px;
    height: 846px;
    overflow: hidden;
    background: var(--page);
  }
  .canvas {
    position: relative;
    width: 1200px;
    height: 846px;
  }
  .label {
    position: absolute;
    left: 416px;
    top: 98px;
    width: 368px;
    height: 651px;
  }
  .honeycomb-field {
    position: absolute;
    inset: 0;
    background: linear-gradient(180deg, var(--honey-light) 0%, var(--honey) 100%);
  }
  .brand {
    position: absolute;
    left: 0;
    right: 0;
    top: 26px;
    display: flex;
    flex-direction: column;
    align-items: center;
    gap: 6px;
  }
  .brand-dot {
    width: 46px;
    height: 46px;
    border-radius: 50%;
    background: var(--white);
  }
  .brand-name {
    font-family: "Stint Ultra Condensed", serif;
    font-size: 24px;
    color: var(--ink);
    letter-spacing: 2px;
    text-transform: uppercase;
  }
  .product-name {
    position: absolute;
    left: 0;
    right: 0;
    top: 146px;
    text-align: center;
    font-family: "Stint Ultra Condensed", serif;
    font-size: 48px;
    line-height: 1;
    letter-spacing: 1px;
    color: var(--ink);
    text-transform: uppercase;
  }
  .seal {
    position: absolute;
    left: 382px;
    top: 306px;
    width: 436px;
    height: 345px;
  }
  .seal-text {
    position: absolute;
    left: 382px;
    top: 306px;
    width: 436px;
    height: 332px;
    display: flex;
    flex-direction: column;
    align-items: center;
    justify-content: center;
    color: var(--white);
    text-align: center;
  }
  .seal-percent {
    font-family: "Permanent Marker", cursive;
    font-size: 104px;
    line-height: 0.9;
    transform: rotate(-6deg);
    margin-top: -30px;
  }
  .seal-claim {
    font-family: "Open Sans", sans-serif;
    line-height: 1.05;
    margin-top: 6px;
  }
  .seal-claim .line-one { display: block; font-size: 22px; }
  .seal-claim .line-two { display: block; font-size: 28px; }
  .origin {
    position: absolute;
    left: 0;
    right: 0;
    top: 560px;
    text-align: center;
    font-family: "Stint Ultra Condensed", serif;
    font-size: 112px;
    line-height: 1;
    letter-spacing: 2px;
    color: var(--ink);
    text-transform: uppercase;
  }
</style>
</head>
<body>
<main class="canvas">
  <section class="label">
    <div class="honeycomb-field" role="img" aria-label="Honeycomb pattern in yellow with scattered white cells"></div>
    <div class="brand">
      <span class="brand-dot"></span>
      <span class="brand-name">Palmetto Hive</span>
    </div>
    <h1 class="product-name">Wildflower Honey</h1>
    <p class="origin">Florida</p>
  </section>

  <svg class="seal" viewBox="0 0 436 345" aria-hidden="true">
    <path d="M218 14 L424 180 L218 344 L12 180 Z" fill="var(--honey-deep)" stroke="var(--honey-deep)" stroke-width="14" stroke-linejoin="round"/>
    <path d="M218 8 L428 166 L218 324 L8 166 Z" fill="var(--ink)" stroke="var(--ink)" stroke-width="14" stroke-linejoin="round"/>
    <path d="M218 26 L404 166 L218 306 L32 166 Z" fill="none" stroke="var(--honey)" stroke-width="2.5"/>
  </svg>

  <div class="seal-text">
    <span class="seal-percent">100%</span>
    <p class="seal-claim">
      <span class="line-one">Pure &amp;</span>
      <span class="line-two">Unfiltered</span>
    </p>
  </div>
</main>
</body>
</html>
```